" A empresa prestará serviços de jardinagem e paisagismo para residencias, condominios e predios comerciais. Fara tanto a elaboraçao dos projetos, como a execuçao dos mesmos e manutençao de jardins. "

```html
<!DOCTYPE html>
<html lang="pt-BR">
<head>
<meta charset="UTF-8">
<title>Verde Lume Paisagismo – Cartão de visita</title>
<link href="https://fonts.googleapis.com/css2?family=Open+Sans:wght@400;600&display=swap" rel="stylesheet">
<style>
  :root {
    --page-bg: #ece8e2;
    --card-dark: #344f2c;
    --card-light: #ffffff;
    --text-on-dark: #f3f5ef;
    --divider: #5f7a55;
    --palm-top: #6f9a5c;
    --palm-bottom: #4d7440;
    --brand-green: #7fb446;
    --brand-purple: #8c3f8f;
    --shadow: rgba(40, 30, 20, 0.28);
  }
  * { box-sizing: border-box; margin: 0; padding: 0; }
  html, body {
    width: 1200px;
    height: 1200px;
    overflow: hidden;
    background: var(--page-bg);
    font-family: "Open Sans", Arial, sans-serif;
  }
  .business-card {
    position: absolute;
    left: 216px;
    width: 768px;
    height: 438px;
    border-radius: 38px;
    box-shadow: 0 10px 26px var(--shadow);
    overflow: hidden;
  }
  .card-back {
    top: 96px;
    background: var(--card-dark);
    color: var(--text-on-dark);
  }
  .card-front {
    top: 670px;
    background: var(--card-light);
  }
  .contact-name {
    position: absolute;
    left: 48px;
    top: 62px;
    font-size: 33px;
    font-weight: 600;
    letter-spacing: 0.2px;
  }
  .contact-role {
    position: absolute;
    left: 110px;
    top: 110px;
    font-size: 16px;
  }
  .contact-phone {
    position: absolute;
    left: 72px;
    top: 134px;
    font-size: 19px;
    letter-spacing: 0.5px;
  }
  .contact-address {
    position: absolute;
    left: 48px;
    top: 252px;
    font-size: 21px;
    line-height: 32px;
    font-style: normal;
  }
  .contact-email {
    position: absolute;
    left: 48px;
    top: 352px;
    font-size: 15px;
  }
  .card-divider {
    position: absolute;
    left: 412px;
    top: 48px;
    width: 2px;
    height: 354px;
    background: var(--divider);
  }
  .palm-decoration {
    position: absolute;
    left: 440px;
    top: 0;
    width: 320px;
    height: 438px;
    background: linear-gradient(180deg, var(--palm-top) 0%, var(--palm-bottom) 100%);
    opacity: 0.55;
    border-radius: 0 38px 38px 0;
  }
  .brand-lockup {
    position: absolute;
    left: 0;
    right: 0;
    top: 150px;
    text-align: center;
  }
  .brand-name-row {
    display: inline-flex;
    align-items: center;
    gap: 16px;
  }
  .brand-mark {
    width: 26px;
    height: 26px;
    border-radius: 50%;
    background: var(--brand-green);
  }
  .brand-name {
    font-size: 66px;
    font-weight: 400;
    color: var(--brand-green);
    line-height: 1;
  }
  .brand-tagline {
    margin-top: 6px;
    font-size: 25px;
    color: var(--brand-purple);
    letter-spacing: 0.5px;
  }
</style>
</head>
<body>
  <section class="business-card card-back" aria-label="Verso do cartão">
    <p class="contact-name">Lívia Moraes</p>
    <p class="contact-role">paisagista</p>
    <p class="contact-phone">(21) 5550 1842</p>
    <address class="contact-address">
      Rua das Acácias, 240<br>
      Bairro - Vila Serena<br>
      Itapira - SP
    </address>
    <p class="contact-email">contato@verdelume.com</p>
    <div class="card-divider"></div>
    <div class="palm-decoration" role="img" aria-label="Silhueta decorativa de palmeira em verde claro"></div>
  </section>

  <section class="business-card card-front" aria-label="Frente do cartão">
    <div class="brand-lockup">
      <div class="brand-name-row">
        <span class="brand-mark"></span>
        <span class="brand-name">Verde Lume</span>
      </div>
      <p class="brand-tagline">paisagismo</p>
    </div>
  </section>
</body>
</html>
```